Digital Album Cover - Piano music for wedding ceremonies and receptions

I need cover art for a piano album project that will be distributed to TuneVault, Streamora etc. Covert art required for front of album. At this stage physical CDs will not be printed nor required it is just a digital release.
Artist name: Leon Harwick
Album Title: Timeless Keys for Vows and Banquet Evenings
Volume 3
Sample piano songs are on my wavehollow page
https://tunevault.example/leonharwickkeys/sets/timeless-keys-vol-3
Previous album artwork used from pixel guild competitions winners
https://musicshelf.example/au/artist/leon-harwick/4830192775
Target Market(s)
brides to be
grooms to be
people interested in weddings
people enjoy love songs or easy listening music
Industry/Entity Type
Wedding
Look and feel

```html
<!DOCTYPE html>
<html lang="en">
<head>
<meta charset="utf-8">
<title>Timeless Keys for Vows and Banquet Evenings — Leon Harwick, Vol. 3</title>
<link rel="stylesheet" href="https://fonts.googleapis.com/css2?family=Bebas+Neue&family=Oswald:wght@400;500&family=Kaushan+Script&display=swap">
<style>
  :root {
    --stage: #171513;
    --photo-dark: #23201d;
    --photo-mid: #6f6255;
    --photo-warm: #d8b999;
    --photo-light: #eee3d6;
    --title-white: rgba(255, 255, 255, 0.9);
    --script-white: #ffffff;
    --caption: #c9cdc9;
    --artist: #e9e6e1;
  }
  * { margin: 0; padding: 0; box-sizing: border-box; }
  html, body {
    width: 1200px;
    height: 960px;
    overflow: hidden;
    background: var(--stage);
  }
  .canvas {
    position: relative;
    width: 1200px;
    height: 960px;
    background: var(--stage);
  }
  .album-cover {
    position: absolute;
    left: 200px;
    top: 80px;
    width: 800px;
    height: 800px;
    overflow: hidden;
  }
  .cover-photo {
    position: absolute;
    inset: 0;
    background: linear-gradient(125deg,
      var(--photo-dark) 0%,
      #3b342e 35%,
      var(--photo-mid) 55%,
      var(--photo-warm) 78%,
      var(--photo-light) 100%);
  }
  .cover-type {
    position: absolute;
    inset: 0;
    width: 800px;
    height: 800px;
  }
  .kicker {
    font-family: "Oswald", sans-serif;
    font-weight: 500;
    font-size: 22px;
    fill: var(--title-white);
  }
  .headline {
    font-family: "Bebas Neue", sans-serif;
    font-size: 470px;
    fill: var(--title-white);
  }
  .script-word {
    font-family: "Kaushan Script", cursive;
    font-size: 118px;
    fill: var(--script-white);
  }
  .subtitle {
    font-family: "Oswald", sans-serif;
    font-weight: 400;
    font-size: 21px;
    letter-spacing: 1px;
    fill: var(--caption);
  }
  .artist-name, .volume {
    font-family: "Bebas Neue", sans-serif;
    fill: var(--artist);
  }
  .artist-name { font-size: 62px; }
  .volume { font-size: 40px; }
  .divider { stroke: var(--artist); stroke-width: 2.5; }
</style>
</head>
<body>
<main class="canvas">
  <section class="album-cover" aria-label="Album cover: Timeless Keys for Vows and Banquet Evenings by Leon Harwick, Volume 3">
    <div class="cover-photo" role="img" aria-label="Warm, sunlit photograph of a groom in a dark suit beside a bride in a white gown holding a bouquet"></div>
    <svg class="cover-type" viewBox="0 0 800 800" xmlns="http://www.w3.org/2000/svg">
      <text class="kicker" x="248" y="170" textLength="315" lengthAdjust="spacing">TIMELESS</text>
      <text class="headline" x="79" y="537" textLength="665" lengthAdjust="spacingAndGlyphs">KEYS</text>
      <text class="script-word" x="330" y="345" text-anchor="middle" transform="rotate(-10 330 330)">for Vows</text>
      <text class="subtitle" x="79" y="590" textLength="313" lengthAdjust="spacingAndGlyphs">AND BANQUET EVENINGS</text>
      <text class="artist-name" x="423" y="616" textLength="232" lengthAdjust="spacingAndGlyphs">LEON HARWICK</text>
      <line class="divider" x1="664" y1="572" x2="664" y2="614"/>
      <text class="volume" x="674" y="604" textLength="78" lengthAdjust="spacingAndGlyphs">VOL. 3</text>
    </svg>
  </section>
</main>
</body>
</html>
```